E-Commerce Website Update for Bamboo Poles Company

Existing website at:

http://www.reedcraftstudio.example/
http://www.reedcraftstudio.example/pages/product-and-price-list

Two pages to design: home page and "price list" page.

Info for home page as follows:

HOME PAGE:

Header:
Company Name: reedcraft studio
Telephone: 1 888 412 5093

Across the top:
Home | Price List | Blog | FAQ | About | Contact

Down the side:
About Bamboo
Wedding Arbors
Bamboo For Flutes
Black Bamboo
Spotted Bamboo
Bamboo Carpentry
Photo Gallery
All Products & Prices
Blog
FAQ
About
Contact

Should have shopping cart and search buttons on top.
Please see ai file, attached for logo (leaf) and font
In addition the homepage should have one or two sections for promotions

Chosen design will be asked to help deign a PRODUCT AND PRICE LIST page similar to the one we have now, but with "LEARN MORE" and "ORDER NOW" buttons for each item.
Updates

Reason: Thanks  for all the designs so far; giving an extra week for extra consideration.

Target Market(s)

Consumers, wedding planners.

Industry/Entity Type

Shopping

Requirements
Must have
• Clean, easy to read design.
Should not have
• No flash animation.

```html
<!DOCTYPE html>
<html lang="en">
<head>
<meta charset="utf-8">
<title>reedcraft studio – Home</title>
<link rel="stylesheet" href="https://fonts.googleapis.com/css2?family=Ubuntu:wght@400;500;700&family=Arimo:wght@400;700&display=swap">
<style>
:root{
  --cream:#f8f6e6;
  --hero:#d7e8d2;
  --green:#75b336;
  --ink:#222;
  --body:#555;
  --footer:#14181c;
  --footer-deep:#0d1013;
  --footer-text:#b9bec4;
}
*{margin:0;padding:0;box-sizing:border-box}
html,body{width:1134px;height:1200px;overflow:hidden;background:var(--cream)}
.page{position:relative;width:1280px;height:1354px;transform:scale(.8859);transform-origin:0 0;font-family:"Arimo",Arial,sans-serif;color:var(--ink)}
.abs{position:absolute}

/* backgrounds */
.header{position:absolute;left:0;top:0;width:1280px;height:134px;background:repeating-linear-gradient(135deg,var(--cream) 0 5px,#f1eed6 5px 6px);z-index:0}
.header-rule{position:absolute;left:0;top:128px;width:1280px;height:6px;background:#a9cd86;z-index:1}
.hero{left:0;top:134px;width:1280px;height:416px;background:var(--hero);z-index:0}
.main{left:0;top:550px;width:1280px;height:525px;background:repeating-linear-gradient(135deg,#fbfaf1 0 5px,#f0eedb 5px 6px);z-index:0}

/* header */
.brand{left:157px;top:18px;font-family:"Ubuntu",sans-serif;font-size:44px;font-weight:500;color:#3a3a3a;letter-spacing:-1px;line-height:1;z-index:2}
.phone-top{right:152px;top:11px;font-family:"Ubuntu",sans-serif;font-size:18px;font-weight:500;color:#222;z-index:2}
.cart{left:955px;top:44px;width:175px;height:58px;z-index:2}
.cart-pill{position:absolute;left:40px;top:10px;width:133px;height:34px;border-radius:17px;background:linear-gradient(#9fd35e,#5fa822);border:1px solid #4f8f1c;color:#fff;font-family:"Ubuntu",sans-serif;font-weight:500;font-size:16px;line-height:32px;text-align:center;padding-left:18px}

/* nav */
.nav{left:150px;top:110px;width:980px;height:42px;border:1px solid #5e9c29;border-radius:3px;background:linear-gradient(#9ccc62,#73b236);z-index:5}
.nav a{position:absolute;top:0;height:40px;line-height:38px;color:#fff;font-family:"Ubuntu",sans-serif;font-size:16px;text-decoration:none;text-align:center}
.nav .sep{position:absolute;top:0;width:1px;height:40px;background:#5f9b2a;box-shadow:1px 0 0 #a7d473}
.search{position:absolute;left:644px;top:7px;width:322px;height:25px;border-radius:13px;background:#eaf2d6;border:1px solid #6ea83a;font-size:12px;color:#555;line-height:23px;padding-left:12px}
.search svg{position:absolute;right:4px;top:3px}

/* hero */
.arrow{z-index:2}
.frame{left:195px;top:174px;width:516px;height:354px;background:#f2f2ef;border:1px solid #c9cfc5;border-radius:4px;z-index:1}
.photo{left:206px;top:185px;width:494px;height:332px;background:linear-gradient(#e4ecf6 0%,#dfe6ee 40%,#c8a66a 62%,#a78450 100%);z-index:2}
.hero-title{left:742px;top:172px;font-family:"Ubuntu",sans-serif;font-weight:500;font-size:23px;line-height:35px;color:#1e1e1e;z-index:2}
.hero-copy{left:746px;top:267px;width:322px;font-size:12px;line-height:22px;color:var(--body);z-index:2}
.hero-copy p+p{margin-top:22px}
.read-more{left:846px;top:443px;width:283px;height:65px;border-radius:18px;background:linear-gradient(#ffffff,#e5e8e4);border:1px solid #cfd5cc;box-shadow:0 3px 3px rgba(0,0,0,.18);z-index:2}
.read-more span{position:absolute;left:31px;top:8px;font-family:"Ubuntu",sans-serif;font-weight:500;font-size:36px;color:#4a9a1c}

/* content */
.divider{left:831px;top:552px;width:1px;height:523px;background:#e1dfca;z-index:1}
.bar{height:35px;color:#fff;font-family:"Ubuntu",sans-serif;font-size:19px;line-height:34px;padding-left:30px;z-index:2}
.bar::before,.bar::after{content:"";position:absolute;top:15px;width:5px;height:5px;border-radius:50%;background:#fff}
.bar::before{left:12px}.bar::after{right:12px}
.bar-products{left:150px;top:567px;width:644px;background:linear-gradient(90deg,#6aad2b,#a8dd7a 55%,#6aad2b)}
.bar-nav{left:847px;top:567px;width:283px;background:linear-gradient(90deg,#1c1e20,#45494d 70%,#1c1e20)}

.card{position:absolute;width:197px;z-index:2}
.card .img{height:121px;border:1px solid #e1e1da}
.card .name{margin-top:14px;padding-left:7px;font-size:12px;color:#555;letter-spacing:.3px}
.card ul{list-style:none;margin-top:10px;padding-left:7px}
.card li{font-family:"Ubuntu",sans-serif;font-size:13px;font-weight:500;color:#222;line-height:18px;padding-left:18px;position:relative}
.card li::before{content:"";position:absolute;left:1px;top:5px;width:7px;height:7px;border-radius:50%;background:#5cae2a}
.card .price{position:absolute;right:8px;bottom:8px;font-family:"Ubuntu",sans-serif;font-size:13px;color:#2f6f0f}

.side-nav{left:853px;top:610px;width:265px;list-style:none;z-index:2}
.side-nav li{height:33px;border-bottom:1px dotted #c9c9bf;font-size:12px;color:#444;line-height:28px;padding-left:22px;position:relative}
.side-nav li svg{position:absolute;left:0;top:7px}

/* footer */
.footer{left:0;top:1075px;width:1280px;height:238px;background:var(--footer)}
.footer-bottom{left:0;top:1313px;width:1280px;height:41px;background:var(--footer-deep);border-top:1px solid #23282d}
.f-title{font-family:"Ubuntu",sans-serif;font-size:17px;color:#fff}
.links{position:absolute;top:1132px;width:191px;list-style:none}
.links li{height:33px;border-top:1px solid #343a40;font-size:12px;color:var(--footer-text);line-height:32px;padding-left:15px;position:relative}
.links li:last-child{border-bottom:1px solid #343a40}
.links li::before{content:"»";position:absolute;left:3px;top:0;font-size:11px}
.contact-rule{left:872px;top:1127px;width:256px;height:5px;background:#33383d}
.contact-name{left:874px;top:1150px;font-family:"Ubuntu",sans-serif;font-size:20px;color:#fff}
.contact-lines{left:874px;top:1177px;font-family:"Ubuntu",sans-serif;font-size:12.5px;line-height:22px;color:#d8dbde}
.copy{left:153px;top:1326px;font-size:10.5px;color:#a7acb1}
.join{left:1004px;top:1325px;font-family:"Ubuntu",sans-serif;font-weight:500;font-size:12px;color:#fff}
.social{position:absolute;top:1325px;width:16px;height:16px;border-radius:2px;background:#3d8fd0}
</style>
</head>
<body>
<div class="page">

  <header class="header"></header>
  <section class="abs hero"></section>
  <section class="abs main"></section>
  <div class="header-rule"></div>

  <div class="abs brand">reedcraft studio</div>
  <div class="abs phone-top">Telephone: 1 888 412 5093</div>
  <div class="abs cart">
    <div class="cart-pill">MY CART</div>
    <svg class="abs" style="left:0;top:0" width="62" height="58" viewBox="0 0 62 58">
      <path d="M2 8 H14 L20 40 H52" fill="none" stroke="#e2e2dc" stroke-width="4" stroke-linecap="round"/>
      <path d="M14 12 H58 L52 34 H19 Z" fill="#f3f3ee" stroke="#c9c9c0" stroke-width="2"/>
      <path d="M56 4 L62 0" stroke="#e55d1a" stroke-width="4"/>
      <circle cx="24" cy="50" r="5" fill="#e55d1a"/>
      <circle cx="46" cy="50" r="5" fill="#e55d1a"/>
    </svg>
  </div>

  <nav class="abs nav">
    <a style="left:0;width:110px">Home</a><span class="sep" style="left:110px"></span>
    <a style="left:111px;width:124px">Price List</a><span class="sep" style="left:235px"></span>
    <a style="left:236px;width:87px">Blog</a><span class="sep" style="left:323px"></span>
    <a style="left:324px;width:84px">FAQ</a><span class="sep" style="left:408px"></span>
    <a style="left:409px;width:106px">About</a><span class="sep" style="left:515px"></span>
    <a style="left:516px;width:112px">Contact</a><span class="sep" style="left:628px"></span>
    <div class="search">Search...
      <svg width="18" height="18" viewBox="0 0 18 18"><circle cx="9" cy="9" r="8.5" fill="#fff" stroke="#aaa"/><circle cx="8" cy="8" r="3" fill="none" stroke="#444" stroke-width="1.5"/><path d="M10 10 L13 13" stroke="#444" stroke-width="2"/></svg>
    </div>
  </nav>

  <svg class="abs arrow" style="left:150px;top:332px" width="26" height="40" viewBox="0 0 26 40"><path d="M22 2 L6 20 L22 38" fill="none" stroke="#3c4750" stroke-width="6"/></svg>
  <svg class="abs arrow" style="left:1105px;top:332px" width="26" height="40" viewBox="0 0 26 40"><path d="M4 2 L20 20 L4 38" fill="none" stroke="#3c4750" stroke-width="6"/></svg>
  <div class="abs frame"></div>
  <div class="abs photo" role="img" aria-label="Bundles of bamboo poles stacked upright in cones in a village yard"></div>
  <h1 class="abs hero-title">Welcome to your Pole Provider<br>1 888 412 5093</h1>
  <div class="abs hero-copy">
    <p>Need bamboo poles at a competitive price? Welcome to your one-stop pole shop.</p>
    <p>We warehouse a variety of types poles in a variety of diameters, from 5/8" to 5 1/2", in lengths up to 8'. We have natural poles, moso (mao) timber poles, black poles spotted poles...</p>
  </div>
  <div class="abs read-more"><span>read more</span>
    <svg class="abs" style="left:210px;top:15px" width="48" height="34" viewBox="0 0 48 34"><path d="M2 11 H26 V2 L46 17 L26 32 V23 H2 Z" fill="#4a9a1c"/></svg>
  </div>

  <div class="abs divider"></div>
  <div class="abs bar bar-products">Products</div>
  <div class="abs bar bar-nav">Navigation</div>

  <div class="card" style="left:150px;top:623px"><div class="img" role="img" aria-label="Close view of tan bamboo poles" style="background:linear-gradient(90deg,#8c6f3e,#d5b57a,#7a5e32,#c9aa6e,#8c6f3e)"></div><div class="name">5 " x 8' Mao Bamboo Poles</div><ul><li>LEARN MORE</li><li>ORDER NOW</li></ul><div class="price">$40.00</div></div>
  <div class="card" style="left:371px;top:623px"><div class="img" role="img" aria-label="Cut piece of pale bamboo with green leaves" style="background:linear-gradient(135deg,#9aa79a,#e0e3d4 50%,#6b7a68)"></div><div class="name">Cutting Bamboo</div><ul><li>LEARN MORE</li><li>ORDER NOW</li></ul><div class="price">$40.00</div></div>
  <div class="card" style="left:597px;top:623px"><div class="img" role="img" aria-label="Two cut bamboo sections lying on white" style="background:linear-gradient(160deg,#f4f4f0,#e3cf9e 55%,#c9a964)"></div><div class="name">Mao Bamboo</div><ul><li>LEARN MORE</li><li>ORDER NOW</li></ul><div class="price">$1400</div></div>
  <div class="card" style="left:150px;top:846px"><div class="img" role="img" aria-label="Bamboo wedding arbor frame on white" style="background:linear-gradient(#f7f4ec,#fbfbf9)"></div><div class="name">Bamboo Wedding Arbor</div><ul><li>LEARN MORE</li><li>ORDER NOW</li></ul><div class="price">$175.00</div></div>
  <div class="card" style="left:371px;top:846px"><div class="img" role="img" aria-label="Yellow-green bamboo poles side by side" style="background:linear-gradient(90deg,#d8e2dc,#c8b45a 25%,#e2d48c 45%,#b59a3e 70%,#d8e2dc)"></div><div class="name">4 pcs 2" x 8' Nan Bamboo Poles</div><ul><li>LEARN MORE</li><li>ORDER NOW</li></ul><div class="price">$24.00</div></div>
  <div class="card" style="left:597px;top:846px"><div class="img" role="img" aria-label="Row of black bamboo poles" style="background:linear-gradient(90deg,#2a2a2a,#5a5a5a,#222,#4a4a4a,#2a2a2a)"></div><div class="name">15 pcs 1" x 8 feet Black Ba...</div><ul><li>LEARN MORE</li><li>ORDER NOW</li></ul><div class="price">$53.25</div></div>

  <ul class="abs side-nav">
    <li><svg width="14" height="14" viewBox="0 0 14 14"><path d="M1 7 L5 12 L13 2" fill="none" stroke="#5cae2a" stroke-width="3"/></svg>About Bamboo</li>
    <li><svg width="14" height="14" viewBox="0 0 14 14"><path d="M1 7 L5 12 L13 2" fill="none" stroke="#5cae2a" stroke-width="3"/></svg>Wedding Arbors</li>
    <li><svg width="14" height="14" viewBox="0 0 14 14"><path d="M1 7 L5 12 L13 2" fill="none" stroke="#5cae2a" stroke-width="3"/></svg>Bamboo For Flutes</li>
    <li><svg width="14" height="14" viewBox="0 0 14 14"><path d="M1 7 L5 12 L13 2" fill="none" stroke="#5cae2a" stroke-width="3"/></svg>Black Bamboo</li>
    <li><svg width="14" height="14" viewBox="0 0 14 14"><path d="M1 7 L5 12 L13 2" fill="none" stroke="#5cae2a" stroke-width="3"/></svg>Spotted Bamboo</li>
    <li><svg width="14" height="14" viewBox="0 0 14 14"><path d="M1 7 L5 12 L13 2" fill="none" stroke="#5cae2a" stroke-width="3"/></svg>Bamboo Carpentry</li>
    <li><svg width="14" height="14" viewBox="0 0 14 14"><path d="M1 7 L5 12 L13 2" fill="none" stroke="#5cae2a" stroke-width="3"/></svg>Photo Gallery</li>
    <li><svg width="14" height="14" viewBox="0 0 14 14"><path d="M1 7 L5 12 L13 2" fill="none" stroke="#5cae2a" stroke-width="3"/></svg>All Products &amp; Prices</li>
    <li><svg width="14" height="14" viewBox="0 0 14 14"><path d="M1 7 L5 12 L13 2" fill="none" stroke="#5cae2a" stroke-width="3"/></svg>Blog</li>
    <li><svg width="14" height="14" viewBox="0 0 14 14"><path d="M1 7 L5 12 L13 2" fill="none" stroke="#5cae2a" stroke-width="3"/></svg>FAQ</li>
    <li><svg width="14" height="14" viewBox="0 0 14 14"><path d="M1 7 L5 12 L13 2" fill="none" stroke="#5cae2a" stroke-width="3"/></svg>About</li>
    <li><svg width="14" height="14" viewBox="0 0 14 14"><path d="M1 7 L5 12 L13 2" fill="none" stroke="#5cae2a" stroke-width="3"/></svg>Contact</li>
  </ul>

  <footer class="abs footer"></footer>
  <div class="abs f-title" style="left:150px;top:1092px">Quick Links</div>
  <ul class="links" style="left:150px"><li>Home</li><li>Price List</li><li>Blog</li><li>FAQ</li></ul>
  <ul class="links" style="left:369px"><li>About</li><li>Contact</li><li>About Bamboo</li><li>Wedding Arbors</li></ul>
  <ul class="links" style="left:593px"><li>Bamboo For Flutes</li><li>Black Bamboo</li><li>Spotted Bamboo</li><li>Bamboo Carpentry</li></ul>
  <div class="abs f-title" style="left:870px;top:1092px">Contact</div>
  <div class="abs contact-rule"></div>
  <div class="abs contact-name">Dana Hollister</div>
  <div class="abs contact-lines">reedcraftstudio.example<br>dana@reedcraftstudio.example<br>(714) 555-0182<br>888 412 5093<br>+86 139 0000 4821</div>

  <div class="abs footer-bottom"></div>
  <div class="abs copy">Copyright © 2011 Reedcraft Studio. All Rights Reserved. All prices USD.</div>
  <div class="abs join">Join US :</div>
  <span class="social" style="left:1061px"></span>
  <span class="social" style="left:1086px;background:#3b5a9a"></span>
  <span class="social" style="left:1112px;background:#2a7ab8"></span>
</div>
</body>
</html>
```